A clean crisp business card for a Landscape Construction company. Designed to be easy to read contact/ info and also be appealing/interesting, unlike a traditional business card.

Industry/Entity Type

Landscape Construction

Contact Information for Business Card

Company name : Bramblecrest Landscape Construction, phone number: (877) 62Vales, website:Bramblecrestlandscapes.example, Email, sales@bramblecrestlandscapes.example

Requirements
Nice to have
• Luxurious finishes/ details…. Icons or emblems next to contact info
Should not have
• Clipart or general pictures

```html
<!DOCTYPE html>
<html lang="en">
<head>
<meta charset="utf-8">
<title>Bramblecrest Landscape Construction – Business Card</title>
<link rel="stylesheet" href="https://fonts.googleapis.com/css2?family=Cinzel:wght@600;700&family=Arimo:wght@400&display=swap">
<style>
  :root {
    --backdrop: #c6c6c6;
    --brand-blue: #1f6bb6;
    --deep-blue: #164f8c;
    --leaf-green: #9ccc2e;
    --paper: #ffffff;
    --ink-light: #ffffff;
  }
  * { box-sizing: border-box; margin: 0; padding: 0; }
  html, body {
    width: 1200px; height: 788px; overflow: hidden;
    background: var(--backdrop);
  }
  .sheet {
    width: 1200px; height: 788px;
    display: flex; align-items: center; justify-content: center; gap: 40px;
  }
  .card {
    position: relative; width: 540px; height: 308px;
    border-radius: 22px; overflow: hidden;
    box-shadow: 0 10px 24px rgba(0,0,0,.25);
  }
  .card--front { background: var(--paper); }
  .card--back { background: var(--brand-blue); }
  .front-shape { position: absolute; inset: 0; }

  .contact-block {
    position: absolute; left: 0; top: 34px; width: 300px;
    color: var(--ink-light); font-family: "Arimo", Arial, sans-serif;
  }
  .person { position: relative; padding-left: 40px; }
  .person::before {
    content: ""; position: absolute; left: 22px; top: 4px;
    width: 9px; height: 40px; background: var(--leaf-green);
  }
  .person__name {
    font-family: "Cinzel", Georgia, serif; font-weight: 700;
    font-size: 22px; color: var(--leaf-green); letter-spacing: .5px; line-height: 1.05;
  }
  .person__role { font-size: 15px; line-height: 1.2; }
  .address { margin: 40px 0 0 40px; font-size: 14px; line-height: 1.35; font-style: normal; }
  .channels { list-style: none; margin: 16px 0 0 40px; font-size: 13.5px; line-height: 1.5; }
  .channels li { display: flex; align-items: center; gap: 8px; white-space: nowrap; }
  .channels svg { width: 12px; height: 12px; flex: none; fill: var(--leaf-green); }

  .brand-front {
    position: absolute; right: 26px; top: 52px; width: 200px; text-align: center;
    font-family: "Cinzel", Georgia, serif; font-weight: 600;
    color: var(--brand-blue);
  }
  .brand-front .brand-dot {
    display: block; width: 14px; height: 14px; border-radius: 50%;
    background: var(--brand-blue); margin: 0 auto 10px;
  }
  .brand-front__name { display: block; font-size: 25px; line-height: 1.1; white-space: nowrap; }
  .brand-front__line {
    display: block; font-size: 10.5px; letter-spacing: 1.6px; line-height: 1.4;
    margin-top: 4px; white-space: nowrap;
  }
  .brand-back {
    position: absolute; right: 40px; top: 40px; text-align: right;
    font-family: "Cinzel", Georgia, serif; font-weight: 700;
    color: var(--deep-blue);
  }
  .brand-back__name { display: block; font-size: 40px; line-height: 1.05; white-space: nowrap; }
  .brand-back__line {
    display: block; font-size: 16px; letter-spacing: 2.5px; line-height: 1.3;
    margin-top: 2px; white-space: nowrap;
  }
</style>
</head>
<body>
<main class="sheet">
  <section class="card card--front" aria-label="Business card front">
    <svg class="front-shape" viewBox="0 0 540 308" aria-hidden="true">
      <path d="M0 0 H250 C252 80 300 140 380 180 C440 212 462 258 452 308 H0 Z" fill="var(--brand-blue)"/>
      <path d="M250 0 C252 80 300 140 380 180 C440 212 462 258 452 308" fill="none" stroke="var(--leaf-green)" stroke-width="4"/>
    </svg>
    <div class="contact-block">
      <div class="person">
        <p class="person__name">DANA MORROW</p>
        <p class="person__role">Founder</p>
      </div>
      <address class="address">418 W. Alder Lane<br>Country Name, AB 35875</address>
      <ul class="channels">
        <li><svg viewBox="0 0 12 12"><path d="M2 1h3l1 3-1.5 1a7 7 0 0 0 2.5 2.5L8 6l3 1v3a1 1 0 0 1-1 1A9 9 0 0 1 1 2a1 1 0 0 1 1-1z"/></svg>(877) 62Vales</li>
        <li><svg viewBox="0 0 12 12"><path d="M0 2h12v1L6 7 0 3z M0 4.5l6 4 6-4V10H0z"/></svg>sales@bramblecrestlandscapes.example</li>
        <li><svg viewBox="0 0 12 12"><circle cx="6" cy="6" r="5.5"/></svg>bramblecrestlandscapes.example</li>
      </ul>
    </div>
    <div class="brand-front">
      <span class="brand-dot"></span>
      <span class="brand-front__name">Bramblecrest</span>
      <span class="brand-front__line">LANDSCAPE CONSTRUCTION</span>
    </div>
  </section>

  <section class="card card--back" aria-label="Business card back">
    <p class="brand-back">
      <span class="brand-back__name">Bramblecrest</span>
      <span class="brand-back__line">LANDSCAPE CONSTRUCTION</span>
    </p>
  </section>
</main>
</body>
</html>
```